Visitenkarten-Design für junges Internetportal
Zielgruppe
Wir vertreiben Freizeitangebote für Kinder. Wir haben unter dem Suchbegriff 'spaßlotsen' ein Erklärvideo bei YouTube. Die Visitenkarte ist zur Gewinnung unserer Partner bestimmt, wie z.B. Sportvereine, Tanzschule, Kreativschulen usw....
Aufgabenstellung
Meine Vorstellung ist eine schlichte Karte.

```html
<!DOCTYPE html>
<html lang="de">
<head>
<meta charset="utf-8">
<title>Spaßlotsen – Visitenkarte</title>
<link rel="stylesheet" href="https://fonts.googleapis.com/css2?family=Open+Sans:wght@400;700&display=swap">
<style>
  :root {
    --teal: #1cc9b4;
    --red: #d9083f;
    --navy: #2a3245;
    --paper: #ffffff;
    --backdrop: #eef0f2;
    --text: #2f3440;
  }
  * { box-sizing: border-box; margin: 0; padding: 0; }
  html, body { width: 1200px; height: 675px; overflow: hidden; }
  body {
    background: var(--backdrop);
    font-family: "Open Sans", Arial, sans-serif;
    color: var(--text);
  }
  .stage {
    position: relative;
    width: 1200px;
    height: 675px;
  }
  .card {
    position: absolute;
    top: 188px;
    width: 520px;
    height: 300px;
    background: var(--paper);
    box-shadow: 0 6px 18px rgba(0,0,0,0.12);
    overflow: hidden;
  }
  .card--contact { left: 60px; }
  .card--brand { left: 620px; }

  .band { position: absolute; height: 14px; }
  .band--teal { background: var(--teal); }
  .band--red { background: var(--red); }

  /* contact side */
  .card--contact .band--top-left { left: 0; width: 190px; top: 62px; }
  .card--contact .band--top-right { left: 262px; right: 0; top: 62px; }
  .card--contact .band--bottom { left: 0; right: 0; bottom: 22px; }
  .brand-dot {
    position: absolute;
    border-radius: 50%;
    background: var(--teal);
  }
  .card--contact .brand-dot { width: 36px; height: 36px; left: 208px; top: 51px; }

  .holder-name {
    position: absolute;
    left: 40px;
    top: 160px;
    font-size: 17px;
    font-weight: 700;
    color: var(--navy);
  }
  .contact {
    position: absolute;
    left: 280px;
    top: 112px;
    font-size: 12.5px;
    line-height: 1.45;
    color: var(--text);
  }
  .contact__company { margin-bottom: 10px; }
  .contact__row { display: flex; }
  .contact__label { width: 62px; }

  /* brand side */
  .card--brand .band--top { left: 0; right: 0; top: 22px; }
  .card--brand .band--bottom { left: 0; right: 0; bottom: 22px; }
  .brand-lockup {
    position: absolute;
    left: 0; right: 0;
    top: 100px;
    display: flex;
    flex-direction: column;
    align-items: center;
    gap: 14px;
  }
  .brand-lockup .brand-dot { position: static; width: 54px; height: 54px; }
  .brand-name {
    font-size: 34px;
    font-weight: 400;
    color: var(--navy);
    letter-spacing: 0.5px;
  }
</style>
</head>
<body>
<main class="stage">
  <section class="card card--contact" aria-label="Visitenkarte Rückseite">
    <div class="band band--teal band--top-left"></div>
    <span class="brand-dot" aria-hidden="true"></span>
    <div class="band band--teal band--top-right"></div>

    <p class="holder-name">Jonas Beispiel</p>

    <div class="contact">
      <p class="contact__company">Spaßlotsen</p>
      <p class="contact__row"><span class="contact__label">Tel.:</span><span>02204 7713582</span></p>
      <p class="contact__row"><span class="contact__label">E-Mail:</span><span>post@spasslotsen.de</span></p>
      <p class="contact__row"><span class="contact__label">Web:</span><span>www.spasslotsen.de</span></p>
      <p class="contact__row"><span class="contact__label">Fbook:</span><span>spaßlotsen</span></p>
    </div>

    <div class="band band--red band--bottom"></div>
  </section>

  <section class="card card--brand" aria-label="Visitenkarte Vorderseite">
    <div class="band band--red band--top"></div>
    <div class="brand-lockup">
      <span class="brand-dot" aria-hidden="true"></span>
      <p class="brand-name">spaßlotsen</p>
    </div>
    <div class="band band--teal band--bottom"></div>
  </section>
</main>
</body>
</html>
```